Pamphlet for introducing people to our church

I would like a church pamphlet designed, that includes the content in file "vosti-pamphlet.txt".

I am looking for a design that will incorporate the content in a professional and creative manner.

You do not have to use the content in any specific order, but I am relying on your skill and design knowledge to organize everything in an artistic and effective way.

Target Market(s)

Everyone

Industry/Entity Type

Religious

Requirements
Must have
• logo, use of content provided, use of branding (logo colors)
Nice to have
• More images where necessary
Should not have
• cross

```html
<!DOCTYPE html>
<html lang="en">
<head>
<meta charset="utf-8">
<title>Vosti Church Pamphlet</title>
<link rel="stylesheet" href="https://fonts.googleapis.com/css2?family=Libre+Baskerville:wght@400;700&family=Tinos:wght@400;700&display=swap">
<style>
  :root {
    --navy: #1f4a6e;
    --orange: #f4a03a;
    --orange-deep: #f39a2e;
    --white: #ffffff;
    --ink: #1b1b1b;
    --backdrop: #e9e4e8;
  }
  * { margin: 0; padding: 0; box-sizing: border-box; }
  html, body { width: 1200px; height: 1037px; overflow: hidden; }
  body { background: var(--backdrop); font-family: "Tinos", serif; }
  .pamphlet {
    position: absolute; left: 253px; top: 28px;
    width: 694px; height: 981px;
    background: var(--white);
    overflow: hidden;
    box-shadow: 0 8px 28px rgba(0,0,0,.18);
  }
  .pamphlet-art { position: absolute; inset: 0; width: 694px; height: 981px; }
  .brand-disc {
    position: absolute; left: 300px; top: -80px;
    width: 230px; height: 230px; border-radius: 50%;
    background: var(--white);
    display: flex; align-items: flex-end; justify-content: center;
    padding-bottom: 60px;
  }
  .brand-name {
    font-family: "Libre Baskerville", serif; font-weight: 400;
    font-size: 48px; color: var(--navy); letter-spacing: 1px;
  }
  .headline-panel {
    position: absolute; left: 95px; top: 240px; width: 520px; height: 150px;
    background: rgba(40,40,40,.55);
    color: var(--white); text-align: center;
    font-family: "Libre Baskerville", serif; font-weight: 700;
  }
  .headline-panel .quote-mark { font-size: 52px; line-height: 40px; display: block; }
  .headline-panel .open { margin-top: 6px; }
  .headline-panel h1 { font-size: 28px; line-height: 36px; font-weight: 700; letter-spacing: .5px; }
  .headline-panel .close { margin-top: 8px; }
  .about {
    position: absolute; left: 318px; top: 545px; width: 345px;
    font-size: 11.2px; line-height: 13.4px; color: var(--ink); text-align: justify;
  }
  .about p + p { margin-top: 10px; }
  .about .lead { font-weight: 700; color: var(--navy); }
  .about .label { font-weight: 700; color: var(--orange-deep); font-size: 13px; }
  .venue {
    position: absolute; left: 348px; top: 792px; width: 310px; height: 48px;
    border: 2px solid var(--navy); border-radius: 24px;
    color: var(--navy); font-weight: 700; font-size: 12px; line-height: 15px;
    text-align: center; padding-top: 8px;
  }
  .venue-pin { position: absolute; left: 145px; top: -18px; background: var(--white); padding: 0 4px; }
  .service {
    position: absolute; left: 28px; top: 822px;
    font-family: "Libre Baskerville", serif; color: var(--navy);
  }
  .service .label { font-family: "Tinos", serif; font-size: 21px; display: block; margin-bottom: 4px; }
  .service .hours { font-size: 28px; font-weight: 700; line-height: 32px; display: block; }
  .web-band {
    position: absolute; left: 0; top: 932px; width: 372px; height: 49px;
    background: var(--navy); color: var(--white);
    font-family: "Libre Baskerville", serif; font-weight: 700; font-size: 20px;
    padding: 13px 0 0 24px;
  }
  .web-band .prompt { color: var(--orange); }
  .contact-band {
    position: absolute; left: 372px; top: 893px; width: 322px; height: 88px;
    background: var(--orange); color: var(--white);
    padding: 10px 14px 0 14px; font-size: 13px; line-height: 16px;
  }
  .contact-band .phone {
    display: flex; align-items: center; gap: 6px;
    font-family: "Libre Baskerville", serif; font-weight: 700; font-size: 24px; line-height: 32px;
  }
  .contact-band .email { font-weight: 700; }
</style>
</head>
<body>
<main class="pamphlet">
  <svg class="pamphlet-art" viewBox="0 0 694 981" xmlns="http://www.w3.org/2000/svg">
    <defs>
      <linearGradient id="photoTone" x1="0" y1="0" x2="0" y2="1">
        <stop offset="0" stop-color="#3d4a5c"/>
        <stop offset="0.4" stop-color="#9a9ca2"/>
        <stop offset="0.55" stop-color="#d9d2c4"/>
        <stop offset="0.72" stop-color="#5e5a45"/>
        <stop offset="1" stop-color="#3f4526"/>
      </linearGradient>
    </defs>
    <path role="img" aria-label="Photograph of a young man praying in a grassy field beneath a sunlit sky"
          d="M0 0 H694 V390 C560 470 400 505 200 505 C120 505 60 498 0 490 Z" fill="url(#photoTone)"/>
    <path d="M250 508 C430 505 580 460 694 398" fill="none" stroke="var(--navy)" stroke-width="9"/>
    <path class="side-band" d="M0 330 C120 420 230 560 280 720 C300 790 300 860 280 932 H0 Z" fill="var(--orange)"/>
  </svg>

  <div class="brand-disc"><span class="brand-name">VOSTI</span></div>

  <section class="headline-panel">
    <span class="quote-mark open">&ldquo;</span>
    <h1>ONE LIGHT FOR EVERY PEOPLE<br>MISSION STATEMENT</h1>
    <span class="quote-mark close">&rdquo;</span>
  </section>

  <section class="about">
    <p><span class="lead">VOSTI</span> is a gathering of believers whose purpose is to seek the face of God for an authentic restoration of the church as a body of born again believers around the world. As a gathering of believers, VOSTI seeks an awakening of the mind founded on the precepts and teachings of Jesus Christ. The modern church has replaced the simple and Kingdom centered principles of Jesus's disciples with complacent and compromised teachings on earthly prosperity. We believe in humbly seeking God without motive to use God or His Word for our own gain. The end times church will experience a glorious revival, renewed love and zeal for true discipleship, faith, and godliness as Jesus intended for us.</p>
    <p><span class="label">MINISTRIES:</span> Little Lanterns (Children's ministry) Children learn to shine with godliness in the world. First Steps Class Learn the basics of Christian faith and about God's purpose for your life. Deeper Roots Class Deepen your knowledge of God's word and learn how to serve him.</p>
  </section>

  <div class="venue">
    <svg class="venue-pin" width="22" height="24" viewBox="0 0 14 20" aria-hidden="true">
      <path d="M7 0C3 0 0 3 0 7c0 5 7 13 7 13s7-8 7-13c0-4-3-7-7-7z" fill="var(--navy)"/>
      <circle cx="7" cy="7" r="2.6" fill="var(--white)"/>
    </svg>
    Linden Hall Community Center, 48 Harbor Row Street,<br>Eastwick, ME 04190
  </div>

  <div class="service">
    <span class="label">Sunday Service:</span>
    <span class="hours">10:00am-</span>
    <span class="hours">12:30pm</span>
  </div>

  <div class="web-band"><span class="prompt">Visit us at</span> www.vosti.org</div>

  <div class="contact-band">
    <div>If you need prayer or counseling give us a call at</div>
    <div class="phone">
      <svg width="20" height="20" viewBox="0 0 24 24" aria-hidden="true">
        <circle cx="12" cy="12" r="11" fill="none" stroke="var(--white)" stroke-width="2"/>
        <path d="M8 6l2 3-1.3 1.3a8 8 0 0 0 5 5L15 14l3 2-1 2.5c-6 0-11-5-11-11z" fill="var(--white)"/>
      </svg>
      +1 207-555-0148
    </div>
    <div>or email us at <span class="email">contact@cedarhollow.org</span></div>
  </div>
</main>
</body>
</html>
```